Flyer-Design für Sabine Wellrath Coaching für Führungskräfte
Zielgruppe
Coaching für Führungskräfte, Seminare für Führungskräfte.
Zielgruppe: Führungskräfte, Unternehmer, Geschäftsführer, Vorstände
Aufgabenstellung
Mein Logo soll beibehalten werden. Es soll ein vierseitiger Flyer sein, der meine Leistungen beschreibt. Es soll sehr modern sein (Stichwort: digital leadership) und seriös. Möglichst nicht das übliche Format, aber nicht zu groß.
Der Text soll weitgehend aus meiner Homepage (www.coaching-wellrath-beispiel.de) übernommen werden, aber es sollen auch zusätzlich Seminare aufgeführt werden.
Bis auf das Logo müssen die angehängten Dateien nicht unbedingt verwendet werden.

```html
<!DOCTYPE html>
<html lang="de">
<head>
<meta charset="utf-8">
<title>Sabine Wellrath – Coaching | Mediation</title>
<link href="https://fonts.googleapis.com/css2?family=Source+Sans+3:ital,wght@0,400;0,600;1,400&display=swap" rel="stylesheet">
<style>
  :root {
    --backdrop: #808080;
    --paper: #ffffff;
    --band: #dde5ef;
    --ink: #2a2a35;
    --accent: #8fa5bf;
    --contact: #3d5f8f;
    --spine: #e6e6e6;
  }
  html, body { margin: 0; padding: 0; }
  body {
    width: 1200px; height: 1200px; overflow: hidden;
    background: var(--backdrop);
    font-family: "Source Sans 3", "Source Sans Pro", sans-serif;
    color: var(--ink);
    position: relative;
  }
  .spread {
    position: absolute; left: 15px; top: 184px;
    width: 1170px; height: 830px;
    background: var(--paper);
  }
  .spine {
    position: absolute; left: 585px; top: 0; width: 1px; height: 100%;
    background: var(--spine);
  }
  .band { position: absolute; top: 0; height: 20px; background: var(--band); }
  .band--left { left: 49px; width: 221px; }
  .band--right { left: 605px; width: 301px; }
  .portrait {
    position: absolute; left: 49px; top: 173px; width: 221px; height: 242px;
    border: 1px solid #9a9a9a; box-sizing: border-box;
    background: radial-gradient(ellipse at 50% 35%, #e9c9a8 0%, #c9a27a 28%, #f4f4f4 55%),
                linear-gradient(#f6f6f6, #8a8a92);
  }
  .quote {
    position: absolute; left: 49px; top: 446px; width: 470px;
    margin: 0; font-size: 24.5px; line-height: 39px; letter-spacing: 0.3px;
    font-weight: 400;
  }
  .quote-author {
    position: absolute; left: 49px; top: 574px; margin: 0;
    font-size: 24.5px; font-style: italic; color: var(--accent); letter-spacing: 0.5px;
  }
  .title {
    position: absolute; left: 605px; top: 75px; margin: 0;
    font-size: 34px; font-weight: 400; letter-spacing: 0.5px;
  }
  .title .sep { margin: 0 4px; }
  .title .accent { color: var(--accent); }
  .column {
    position: absolute; top: 170px; width: 172px;
    font-size: 12px; line-height: 21px;
  }
  .column p { margin: 0 0 21px; }
  .column strong { font-weight: 600; }
  .column--one { left: 605px; }
  .column--two { left: 792px; }
  .column--three { left: 979px; }
  .contact { color: var(--contact); }
</style>
</head>
<body>
  <div class="spread">
    <div class="spine"></div>
    <div class="band band--left"></div>
    <div class="band band--right"></div>

    <div class="portrait" role="img" aria-label="Porträtfoto von Sabine Wellrath"></div>
    <p class="quote">In jedem Menschen steckt alles Nötige, um ein glückliches und erfolgreiches Leben zu führen.</p>
    <p class="quote-author">Sabine Wellrath</p>

    <h1 class="title">Coaching<span class="sep">|</span><span class="accent">Mediation</span></h1>

    <div class="column column--one">
      <p>Sie suchen individuelle Lösungen für Konfliktsituationen oder berufliche Herausforderungen mit der Hilfe von Coaching oder Mediation? Als Coach und Mediatorin mit langjähriger, eigener Erfahrung als Führungskraft, unterstütze ich hierbei Privatpersonen, Führungskräfte und Unternehmen. Gemeinsam machen wir uns an die Arbeit und entwickeln Wege zur Verwirklichung Ihrer persönlichen Ziele!</p>
      <p><strong>Mein Business Coaching-Angebot richtet sich an Personen mit Führungsverantwortung und/ oder im Management und an Unternehmen.</strong></p>
      <p>Der Führungsstil hat einen erheblichen Einfluss auf den Erfolg einer Organisation. Eine gute Führung der Mitarbeiter sorgt in der Regel für Zufriedenheit, Motivation und Engagement.</p>
    </div>

    <div class="column column--two">
      <p>Dies wirkt sich wiederum positiv auf die Kundenzufriedenheit aus. Somit sollten Sie für Ihren beruflichen Weg über ein Coaching nachdenken, denn schon eine kleine Veränderung im Führungsstil kann Ihren Mitarbeitern mehr entlocken. Mit meinem Training können Sie Ihre Führungskompetenz stärken und/oder neue Stärken entwickeln.</p>
      <p><strong>Mein Angebot für Mediation richtet sich an Konfliktparteien, die an einer konstruktiven Beilegung interessiert sind.</strong></p>
      <p>Menschen brauchen soziale Beziehungen, um ein zufriedenes oder glückliches Leben führen zu können. Beziehungen und arbeiten im Team bedeutet aber immer auch zumindest mögliche Konflikte. Konflikte können im Nachhinein als Bereicherung wahrgenommen werden, an</p>
    </div>

    <div class="column column--three">
      <p>denen der Mensch wächst. Im gegenwärtigen Erleben kann ein Konflikt unlösbar erscheinen und Kraft binden. Es kann dann hilfreich sein, sich bei der Lösung des Konfliktes Hilfe zu suchen. Um zu einer Lösung zu finden, bei der es keine Verlierer gibt, biete ich Ihnen Mediation an. Hierbei nehme ich mir Zeit, um mit meinem geschulten Blick von Aussen eine Lösung zu finden, bei der Ihre eigenen Ziele und die der anderen Partei berücksichtigt werden.</p>
      <p class="contact">Bei Fragen oder Interesse an einer Beratung schreiben Sie mir per Mail oder rufen Sie mich direkt an unter 0170 44129836. Gerne können wir Termine vereinbaren, ich freue mich auf Sie!</p>
    </div>
  </div>
</body>
</html>
```